Vellmora Harvest Online organic artisan and gourmet supermarket

Brief:
Brand: Vellmora Harvest (VH) is an online store selling artisan and organinc Italian products. Our look and feel we have gone with is rustic, premium and unfiltered (visit us @ www.vellmoraharvest.com.au)
Our slogan: "cook Italy, eat Italy, love Italy"
Goals: prior to our online store going live, we used to attend a food market once a week. Due to unfortunate circumstances, we stopped. Since then, our store has gone live and wanted to use the card as a reminder we are back at the markets.
I also have a restaurant, "vellmora ristorante" so I wanted to hand them out to customers in the restaurant but also act as reminder of our pop up market stores and our website to buy from.
Personality: VH is more than just a store. Our goal is to be not only a store but an informationa hub of Italian food.
We offer assistance to people who need help in their kitchen as well as catering
Logo: I have a logo which I was not able to upload.

Target Market(s)

Food lovers
Italian food interest
Wealthy
Organic gourmet food enthusiest

Industry/Entity Type

Store

Contact Information for Business Card

Shop online or visit us @ Birchwell Hollow organic market
Ciao@vellmoraharvest.com.au
Www.vellmoraharvest.com.au

Online store, Cooking advice, catering, ristorante and information hub

Requirements
Must have
• Logo
• Information
• May be larger than a business card to fit information but smaller than a post card
• Need to look interesting and different
• Not a simple card design
Nice to have
• Different fonts
• Rustic looking
• Qwerky

```html
<!DOCTYPE html>
<html lang="en">
<head>
<meta charset="utf-8">
<title>Vellmora Harvest – Business Card</title>
<link href="https://fonts.googleapis.com/css2?family=Cinzel:wght@600;700&family=Quicksand:wght@400;700&family=Carlito&display=swap" rel="stylesheet">
<style>
  :root{
    --backdrop:#3b3937;
    --card-dark:#15211d;
    --band-dark:#171c1a;
    --paper:#ffffff;
    --ink:#1a1a1a;
    --accent-red:#d6283a;
    --accent-orange:#f07a3c;
    --accent-green:#2f9d5a;
    --line:#2a2a2a;
    --light-text:#f2f2f2;
  }
  html,body{margin:0;padding:0;overflow:hidden}
  body{width:1200px;height:1200px;background:var(--backdrop);position:relative}
  .card{position:absolute;left:170px;width:860px;height:524px;box-shadow:0 8px 24px rgba(0,0,0,.35);overflow:hidden}

  /* back side */
  .card-back{top:46px;background:radial-gradient(circle at 50% 40%, #1c2b26 0%, var(--card-dark) 70%)}
  .brand-seal{position:absolute;left:290px;top:40px;width:280px;height:280px;border:3px solid var(--light-text);border-radius:50%;display:flex;align-items:center;justify-content:center}
  .brand-seal .brand-name{font-family:"Cinzel",serif;font-weight:700;font-size:30px;color:var(--light-text);letter-spacing:2px;text-align:center;line-height:1.2}
  .services{position:absolute;left:0;right:0;top:345px;text-align:center;font-family:"Quicksand",sans-serif;font-size:17px;letter-spacing:3px;color:var(--light-text);text-transform:uppercase}
  .visit{position:absolute;right:60px;bottom:58px;text-align:right;font-family:"Quicksand",sans-serif;color:var(--light-text);font-size:22px;line-height:1.45}
  .visit .market-name{color:var(--accent-orange);font-weight:700}
  .visit .market-type{font-weight:700}

  /* front side */
  .card-front{top:630px;background:var(--paper)}
  .front-seal{position:absolute;left:40px;top:26px;width:170px;height:170px;border:2px solid var(--ink);border-radius:50%;display:flex;align-items:center;justify-content:center}
  .front-seal .brand-name{font-family:"Cinzel",serif;font-weight:700;font-size:17px;color:var(--ink);text-align:center;line-height:1.25;letter-spacing:1px}
  .title{position:absolute;left:290px;top:78px;font-family:"Cinzel",serif;font-weight:700;font-size:38px;letter-spacing:3px;color:var(--ink)}
  .slogan{position:absolute;left:292px;top:132px;font-family:"Cinzel",serif;font-weight:600;font-size:19px;letter-spacing:.5px;color:var(--ink)}
  .rule{position:absolute;height:1.5px;background:var(--line)}
  .rule-top{left:0;right:0;top:222px}
  .rule-lower{left:420px;right:0;top:360px}
  .person{position:absolute;left:40px;top:196px;background:var(--paper);padding:0 12px}
  .person-name{font-family:"Cinzel",serif;font-weight:700;font-size:28px;color:var(--accent-red);letter-spacing:1px;line-height:1}
  .person-role{font-family:"Carlito",sans-serif;font-size:15px;color:var(--ink);margin-top:4px;text-transform:uppercase}
  .contact-band{position:absolute;left:0;top:262px;width:420px;bottom:0;background:var(--band-dark)}
  .bottom-band{position:absolute;left:0;right:0;top:380px;bottom:0;background:var(--band-dark)}
  .food-photo{position:absolute;left:420px;right:0;top:380px;bottom:0;background:linear-gradient(90deg,var(--band-dark) 0%,#3b2e24 35%,#6a4e36 65%,#8a6a4c 100%)}
  .contacts{position:absolute;left:40px;top:280px;margin:0;padding:0;list-style:none;font-family:"Carlito",sans-serif;font-size:18px;color:var(--light-text);line-height:30px}
  .contacts li{display:flex;align-items:center;gap:12px}
  .contacts svg{width:17px;height:17px;flex:none}
  .address{position:absolute;left:22px;top:418px;font-family:"Carlito",sans-serif;font-size:18px;color:var(--light-text);text-transform:uppercase}
</style>
</head>
<body>

<section class="card card-back">
  <div class="brand-seal"><span class="brand-name">Vellmora<br>Harvest</span></div>
  <p class="services">Cooking advice · Catering · Ristorante · Information hub · Online store</p>
  <div class="visit">
    Shop online or visit us @ <span class="market-name">Birchwell Hollow</span> <span class="market-type">organic market</span><br>
    www.vellmoraharvest.com.au
  </div>
</section>

<section class="card card-front">
  <div class="front-seal"><span class="brand-name">Vellmora<br>Harvest</span></div>
  <div class="title">VELLMORA HARVEST</div>
  <div class="slogan">COOK ITALY, EAT ITALY, LOVE ITALY</div>

  <div class="contact-band"></div>
  <div class="bottom-band"></div>
  <div class="food-photo" role="img" aria-label="Photo of Italian antipasto on a wooden board: olives, prosciutto, cheese and bread"></div>

  <div class="rule rule-top"></div>
  <div class="rule rule-lower"></div>

  <div class="person">
    <div class="person-name">Marco Bellini</div>
    <div class="person-role">Director</div>
  </div>

  <ul class="contacts">
    <li><svg viewBox="0 0 20 20"><circle cx="10" cy="10" r="10" fill="var(--accent-green)"/><path d="M7 5l2 2-1 1.5c.8 1.6 2 2.8 3.5 3.5L13 11l2 2-1.5 1.8C10 14.5 5.5 10 5.2 6.5z" fill="#fff"/></svg>Toll free: (02) 5550 1437</li>
    <li><svg viewBox="0 0 20 20"><circle cx="10" cy="10" r="10" fill="var(--accent-green)"/><rect x="5" y="6.5" width="10" height="7" fill="#fff"/><path d="M5 6.5l5 4 5-4" stroke="var(--accent-green)" stroke-width="1.2" fill="none"/></svg>ciao@vellmoraharvest.com.au</li>
    <li><svg viewBox="0 0 20 20"><circle cx="10" cy="10" r="10" fill="var(--accent-green)"/><g fill="none" stroke="#fff" stroke-width="1.2"><circle cx="10" cy="10" r="5.5"/><ellipse cx="10" cy="10" rx="2.5" ry="5.5"/><path d="M4.5 10h11"/></g></svg>www.vellmoraharvest.com.au</li>
  </ul>
  <div class="address">48 Corliss Lane, Tarrowby, 2190</div>
</section>

</body>
</html>
```